Coaching Services Flyer

I need a two page flyer to promote by coaching (life and business coaching services) something like this: http://brightlanterncove.example/downloads/Dana-Rourke-Workshops-and-Coaching-2015.pdf

My primary client is small business owners who are looking for help reaching their business goals.

Please incorporate my logo below and if possible, the compass symbol. I want something that speaks to finding your direction. The colors are bold so the design needs to soften the overall look a bit since it's a coaching service.

Also incorporate the quote from Kallinor: “Excellence is never an accident. It is always the result of high intention, sincere effort, and intelligent execution; it represents the wise choice of many alternatives - choice, not chance, determines your destiny.”

```html
<!DOCTYPE html>
<html lang="en">
<head>
<meta charset="utf-8">
<title>Harwick Coaching Services Flyer</title>
<link href="https://fonts.googleapis.com/css2?family=Fredericka+the+Great&family=Open+Sans:ital,wght@0,300;0,400;0,600;0,700;1,300;1,400&display=swap" rel="stylesheet">
<style>
  :root {
    --backdrop: #d9c4a2;
    --paper: #ffffff;
    --brand-red: #d31212;
    --brand-navy: #15197a;
    --ink: #111111;
    --band: #000000;
    --frame-shadow: #cfcfcf;
  }
  * { box-sizing: border-box; margin: 0; padding: 0; }
  html, body {
    width: 1200px; height: 1200px; overflow: hidden;
    background: var(--backdrop);
    font-family: "Open Sans", Arial, sans-serif;
  }
  .flyer {
    position: absolute; left: 160px; top: 30px;
    width: 994px; height: 1286px;
    background: var(--paper);
    transform: scale(0.8865); transform-origin: 0 0;
    box-shadow: 0 4px 14px rgba(0,0,0,.25);
  }
  .rule { position: absolute; left: 23px; width: 947px; }
  .rule--red { background: var(--brand-red); }
  .rule--navy { background: var(--brand-navy); }

  .flyer__title {
    position: absolute; top: 82px; left: 0; width: 100%;
    text-align: center;
    font-family: "Fredericka the Great", "Georgia", serif;
    font-size: 62px; font-weight: 400; color: var(--ink);
    letter-spacing: 1px;
  }
  .portrait {
    position: absolute; left: 46px; top: 210px; width: 216px; height: 284px;
    border: 2px solid #333; background: #fff;
    box-shadow: 5px 5px 0 var(--frame-shadow);
  }
  .intro {
    position: absolute; left: 307px; top: 212px; width: 642px;
    font-size: 16.2px; line-height: 18px; color: var(--ink);
  }
  .intro p + p { margin-top: 18px; }

  .quote-band {
    position: absolute; left: 23px; top: 517px; width: 947px; height: 126px;
    background: var(--band); color: #fff;
    display: flex; align-items: center; justify-content: center;
    text-align: center;
    font-style: italic; font-weight: 400; font-size: 24px; line-height: 31px;
  }

  .details {
    position: absolute; left: 46px; top: 668px; width: 630px;
    color: var(--brand-navy); font-size: 16.2px; line-height: 18px;
  }
  .details p { margin-bottom: 15px; }
  .details ul { list-style: none; margin-bottom: 15px; }
  .details li { position: relative; padding-left: 21px; line-height: 16.2px; }
  .details li::before, .workshops li::before {
    content: ""; position: absolute; left: 1px; top: 5px;
    width: 10px; height: 10px; background: currentColor;
  }

  .workshops {
    position: absolute; left: 709px; top: 666px; width: 238px; height: 255px;
    background: var(--brand-red); color: #fff;
    padding: 20px 0 0 23px;
  }
  .workshops h2 { font-size: 16.5px; font-weight: 700; margin-bottom: 17px; }
  .workshops ul { list-style: none; }
  .workshops li {
    position: relative; padding-left: 17px;
    font-size: 16.2px; line-height: 18px;
  }
  .workshops li::before { top: 4px; }
  .accent-block {
    position: absolute; left: 709px; top: 945px; width: 238px; height: 130px;
    background: var(--brand-red);
  }

  .contact {
    position: absolute; right: 432px; top: 1127px;
    text-align: right; color: var(--brand-navy);
    font-size: 19px; line-height: 27px; font-style: normal;
  }
  .contact__name { font-weight: 700; }
  .contact strong { font-weight: 700; }

  .brand {
    position: absolute; left: 597px; top: 1118px; width: 350px;
    font-size: 92px; font-weight: 400; color: var(--ink);
    line-height: 110px; letter-spacing: -2px; text-align: center;
  }
</style>
</head>
<body>
  <main class="flyer">
    <div class="rule rule--red" style="top:46px;height:6px"></div>
    <div class="rule rule--red" style="top:56px;height:3px"></div>

    <h1 class="flyer__title">Your Name Goes Here</h1>

    <div class="rule rule--navy" style="top:173px;height:3px"></div>
    <div class="rule rule--navy" style="top:180px;height:6px"></div>

    <div class="portrait" role="img" aria-label="Portrait photo of the coach"></div>

    <section class="intro">
      <p>Lorem ipsum dolor sit amet. Aliquyam sed odio. Amet sadipscing mazim ipsum praesent labore. Et dolores voluptua. Dolore et praesent molestie. Feugiat amet qui odio quod stet. Sit diam feugiat. Stet eos ipsum sea euismod. Labore illum wisi ea at. Lorem invidunt est sanctus gubergren molestie. Est liber ea ipsum. Consetetur diam dolor at kasd sed rebum tempor. Te est facilisis no lorem no veniam. Et nonumy elit rebum. Sea diam voluptua ut. Enim takimata vero dolore clita.</p>
      <p>Dolores in ut duo et tation. Odio soluta nonumy qui praesent stet sit eirmod. Eos accumsan elitr takimata duis illum gubergren. Voluptua dolor vero nobis magna et erat eum. Est nam et dolores accusam et. Sit praesent dolore autem no praesent no possim. Aliquyam lorem vero in. Option nulla stet takimata diam. Gubergren lorem vulputate illum. Et eirmod dolore. Dolore eleifend invidunt. Lorem erat autem facilisis. Illum eum aliquam vulputate. Vero et diam zzril dolore delenit. Vulputate in ut elitr. Est aliquyam praesent diam stet amet.</p>
    </section>

    <blockquote class="quote-band">
      <p>“Excellence is never an accident. It is always the result of high intention,<br>sincere effort, and intelligent execution; it represents the wise choice<br>of many alternatives - choice, not chance, determines your destiny.”</p>
    </blockquote>

    <section class="details">
      <p>Lorem ipsum dolor sit amet. Labore amet feugait. Iusto vel magna. Molestie amet voluptua lorem dolore. Duo dolore ipsum. Te sanctus nisl. Sanctus et duo eos kasd et sit rebum. Dolor gubergren sed dolore nonumy duo sed. Elitr gubergren labore laoreet eirmod takimata nonumy. No praesent consetetur sanctus eos kasd enim diam. Sea et no dolor tempor.</p>
      <ul>
        <li>Consequat commodo duis sed et eirmod sanctus.</li>
        <li>Ut consetetur et. Ut in ea exerci dolores.</li>
        <li>Aliquam nihil est.</li>
        <li>Dolor illum clita consetetur accusam.</li>
        <li>Esse sanctus ipsum augue euismod.</li>
      </ul>
      <p>Dolores lorem rebum eirmod vel eros. Sea vero tempor dolores duis esse sea ad. Suscipit amet quis ea.</p>
      <p>Facilisis et elitr justo sed et. Ea clita erat invidunt. Stet tempor duo esse facilisi eos labore sed. Ad est dolor tempor sed voluptua ex iriure. Nonumy est consetetur no lorem ea lobortis ea. Illum euismod luptatum. Accumsan accusam sanctus duo eos nostrud eleifend vel. Lobortis gubergren diam clita nostrud. Dolore sanctus diam consequat in elitr ea.</p>
      <ul>
        <li>Amet nulla dolore diam erat odio magna.</li>
        <li>Invidunt erat sea sadipscing accusam et dolore.</li>
      </ul>
    </section>

    <aside class="workshops">
      <h2>Workshops available</h2>
      <ul>
        <li>Marketing / Branding</li>
        <li>Time Management</li>
        <li>Strategic Planning</li>
        <li>Communications</li>
        <li>Goal-Setting &amp; Planning</li>
        <li>Entrepreneurship</li>
        <li>Getting Organized</li>
        <li>Leadership</li>
        <li>Board Development<br>&amp; Governance</li>
      </ul>
    </aside>
    <div class="accent-block"></div>

    <div class="rule rule--red" style="top:1099px;height:6px"></div>
    <div class="rule rule--red" style="top:1109px;height:3px"></div>

    <address class="contact">
      <div class="contact__name">Your Name Goes Here - Harwick Coaching Services</div>
      <div>#1234, Ferncliff, Nova Scotia, Canada B4Z 2K7</div>
      <div>Phone: <strong>000.000.0000</strong> E-mail: <strong>info@harwick.example</strong></div>
    </address>

    <div class="brand">Harwick</div>

    <div class="rule rule--navy" style="top:1225px;height:3px"></div>
    <div class="rule rule--navy" style="top:1232px;height:6px"></div>
  </main>
</body>
</html>
```